Mobile Physiotherapy Service Flyer

Create a flyer that is eye catching and leave an impression on people’s minds.

Flyer should portray Harbor Stride Mobile’s values
-An attitude and service that is above and beyond
-Quality and current physiotherapy practices
-Reliability- service that people can trust

Flyer should also make it obvious that Harbor Stride Mobile (HSM) is a home visiting physiotherapy service.
Flyer should also indicate the types of services provided by HSM
-Falls prevention
-Help older people stay in their own home (instead of going to live in a nursing home)
-Amputee rehabilitation
Orthopaedic rehabilitation (shoulder, knees, hips)
-Neurological rehabilitation (stroke, head injuries, spinal cord injuries, MS, MND, Parkinson’s disease)
-Emergency physiotherapy

Flyer should appeal to target population: -
-Over 65’s
-People with disabilities
-Busy working adults and/or busy young families

HSM Contact details: -
Phone number: 1300 418 267
Email: mobile@harborstridephysio.com.au

HSM colour scheme: -
White and Blue
Our logo and colour scheme is as attached in the file.

You can visit our website at http://www.harborstridephysio.com.au/mobile to have a look at our services in depth.

Previous flyer has been attached for an idea, but we want something fresh and exciting that people will remember.

Target Market(s)

The Elderly, people who suffer from severe motor vehicle accidents, people who has just had an operation, People who suffer from neurological disorders such as Parkinson's, stroke, Amputees.

Industry/Entity Type

Health Care

Colors
33a6d7

Requirements
Must have
• Must have our Contact details and our logo.
• Harbor Stride Mobile Contact details: -
• Phone number: 1300 418 267
• Email: mobile@harborstridephysio.com.au
• and description of our services we provide
Nice to have
• Photos/pictures
Should not have
• do not want to have something similar to the old brochure. want something that people will be interested to read and look at.

```html
<!DOCTYPE html>
<html lang="en">
<head>
<meta charset="utf-8">
<title>Harbor Stride Mobile – Physio That Moves You</title>
<link href="https://fonts.googleapis.com/css2?family=Teko:wght@500&family=Open+Sans:wght@400;600;700;800&display=swap" rel="stylesheet">
<style>
  :root {
    --brand-blue: #33a6d7;
    --bright-blue: #1fa6dc;
    --charcoal: #58595b;
    --ink: #1a1a1a;
    --white: #ffffff;
    --sea-deep: #2a7f78;
    --sea-light: #9fd0e0;
    --skin-soft: #e8d9cf;
  }
  html, body {
    margin: 0;
    padding: 0;
    width: 720px;
    height: 1200px;
    overflow: hidden;
    background: #ffffff;
  }
  .flyer {
    position: relative;
    width: 720px;
    height: 1200px;
    overflow: hidden;
    background: var(--white);
    font-family: "Open Sans", Arial, sans-serif;
  }
  .flyer-graphics {
    position: absolute;
    inset: 0;
  }
  .brand {
    position: absolute;
    left: 58px;
    top: 462px;
    display: flex;
    align-items: center;
    gap: 10px;
  }
  .brand-dot {
    width: 22px;
    height: 22px;
    border-radius: 50%;
    background: var(--bright-blue);
  }
  .brand-name {
    font-family: "Open Sans", Arial, sans-serif;
    font-weight: 700;
    font-size: 25px;
    color: var(--bright-blue);
    letter-spacing: -0.3px;
  }
  .headline {
    position: absolute;
    left: 0;
    width: 720px;
    text-align: center;
    margin: 0;
  }
  .headline-main {
    top: 566px;
    font-family: "Teko", "Oswald", sans-serif;
    font-weight: 500;
    font-size: 118px;
    line-height: 1;
    color: var(--bright-blue);
    letter-spacing: 2px;
  }
  .headline-sub {
    top: 690px;
    font-family: "Open Sans", Arial, sans-serif;
    font-weight: 800;
    font-size: 56px;
    line-height: 1;
    color: var(--ink);
  }
  .tagline {
    position: absolute;
    left: 92px;
    top: 756px;
    width: 478px;
    height: 38px;
    border-radius: 19px;
    background: var(--charcoal);
    color: var(--white);
    font-weight: 600;
    font-size: 22px;
    line-height: 38px;
    text-align: center;
  }
  .services {
    position: absolute;
    left: 62px;
    top: 828px;
    color: var(--white);
  }
  .services-title {
    margin: 0 0 6px;
    font-weight: 700;
    font-size: 26px;
    line-height: 1.3;
  }
  .service-list {
    list-style: none;
    margin: 0;
    padding: 0;
  }
  .service-item {
    position: relative;
    padding-left: 28px;
    margin-bottom: 8px;
    font-size: 19px;
    line-height: 1.22;
  }
  .service-item:last-child { margin-bottom: 0; }
  .service-item::before {
    content: "";
    position: absolute;
    left: 2px;
    top: 6px;
    width: 11px;
    height: 11px;
    border-radius: 50%;
    background: var(--white);
  }
  .contact {
    position: absolute;
    left: 0;
    width: 720px;
    text-align: center;
  }
  .contact-phone {
    top: 1128px;
    display: flex;
    justify-content: center;
    align-items: center;
    gap: 10px;
    font-family: "Teko", "Oswald", sans-serif;
    font-weight: 500;
    font-size: 40px;
    line-height: 1;
    color: var(--bright-blue);
  }
  .contact-phone svg { margin-top: -6px; }
  .contact-email {
    top: 1166px;
    font-size: 18px;
    letter-spacing: 3.2px;
    color: var(--white);
  }
</style>
</head>
<body>
<main class="flyer">
  <svg class="flyer-graphics" width="720" height="1200" viewBox="0 0 720 1200">
    <defs>
      <linearGradient id="surf-photo" x1="0" y1="0" x2="0" y2="1">
        <stop offset="0" stop-color="#cfe2ea"/>
        <stop offset="0.45" stop-color="#9fd0e0"/>
        <stop offset="0.75" stop-color="#3a9a8c"/>
        <stop offset="1" stop-color="#2a7f78"/>
      </linearGradient>
      <linearGradient id="stretch-photo" x1="0" y1="0" x2="0" y2="1">
        <stop offset="0" stop-color="#f4f4f4"/>
        <stop offset="1" stop-color="#e8d9cf"/>
      </linearGradient>
    </defs>

    <circle cx="440" cy="90" r="372" fill="none" stroke="var(--charcoal)" stroke-width="18"/>
    <circle cx="440" cy="90" r="350" fill="none" stroke="var(--bright-blue)" stroke-width="10"/>
    <circle cx="440" cy="90" r="336" fill="url(#surf-photo)" role="img" aria-label="Photo of a surfer riding a breaking wave"/>

    <path d="M0 770 Q360 850 720 860 L720 1200 L0 1200 Z" fill="var(--bright-blue)"/>
    <path d="M0 788 Q360 830 720 855" fill="none" stroke="var(--charcoal)" stroke-width="6"/>
    <path d="M0 760 Q360 810 720 838 L720 852 Q360 824 0 782 Z" fill="var(--white)"/>

    <rect x="0" y="1120" width="720" height="80" fill="var(--charcoal)"/>
    <rect x="0" y="1116" width="720" height="4" fill="var(--white)"/>

    <circle cx="548" cy="410" r="182" fill="var(--white)"/>
    <circle cx="548" cy="410" r="172" fill="none" stroke="var(--charcoal)" stroke-width="12"/>
    <circle cx="548" cy="410" r="156" fill="none" stroke="var(--bright-blue)" stroke-width="8"/>
    <circle cx="548" cy="410" r="146" fill="url(#stretch-photo)" role="img" aria-label="Photo of a woman doing a seated spinal twist stretch on a mat"/>
  </svg>

  <div class="brand">
    <span class="brand-dot"></span>
    <span class="brand-name">Harbor Stride Mobile</span>
  </div>

  <h1 class="headline headline-main">PHYSIO THAT</h1>
  <p class="headline headline-sub">MOVES YOU</p>
  <p class="tagline">TO YOUR BEST QUALITY OF LIFE</p>

  <section class="services">
    <h2 class="services-title">Service</h2>
    <ul class="service-list">
      <li class="service-item">Falls prevention</li>
      <li class="service-item">Help older people stay in their own home<br>(instead of going to live in a nursing home)</li>
      <li class="service-item">Amputee rehabilitation<br>Orthopaedic rehabilitation (shoulder, knees, hips)</li>
      <li class="service-item">Neurological rehabilitation (stroke, head injuries<br>spinal cord injuries, MS, MND, Parkinson’s disease)</li>
      <li class="service-item">Emergency physiotherapy</li>
    </ul>
  </section>

  <div class="contact contact-phone">
    <svg width="26" height="26" viewBox="0 0 26 26" aria-hidden="true">
      <rect x="0" y="0" width="26" height="26" rx="6" fill="var(--bright-blue)"/>
      <path d="M8 6c1 0 2 2.5 2 3.2s-1.2 1.1-1 1.8c.6 2 2.3 3.8 4.3 4.5.7.2 1.1-1 1.8-1s3.1 1 3.1 2c0 1.4-1.6 2.5-3 2.5C10 19 7 16 6 9.8 5.8 7.5 7 6 8 6z" fill="var(--charcoal)"/>
    </svg>
    <span>1300 418 267</span>
  </div>
  <div class="contact contact-email">mobile@harborstridephysio.com.au</div>
</main>
</body>
</html>
```